Brochure for Security Guard and Video Monitoring Services

I need a brochure design so I can hand our brochures to prospects at a trade show. I will provide my company logo and some content and a few pictures to put into the brochure design. I am open to you adding other stock photos if you feel it can help the look of the brochure. Logo provided in .png and .eps

Industry/Entity Type

It Company

Requirements
Must have
• Few photos.

```html
<!DOCTYPE html>
<html lang="en">
<head>
<meta charset="utf-8">
<title>Rampart Group — Live Video Monitoring</title>
<link href="https://fonts.googleapis.com/css2?family=Montserrat:wght@400;600;700&display=swap" rel="stylesheet">
<style>
  :root {
    --red: #c0201b;
    --red-deep: #b10f12;
    --red-overlay: rgba(200, 30, 22, 0.88);
    --paper: #f2f2f2;
    --ink: #3a3a3a;
    --white: #ffffff;
    --stage: #c9ccca;
    --photo-light: #d6d6d6;
    --photo-dark: #8d8d8d;
  }
  * { box-sizing: border-box; margin: 0; padding: 0; }
  html, body {
    width: 1200px; height: 1013px; overflow: hidden;
    background: var(--stage);
    font-family: "Montserrat", sans-serif;
  }
  .flyer {
    position: absolute; left: 265px; top: 26px;
    width: 670px; height: 960px;
    background: var(--paper);
    overflow: hidden;
  }
  .flyer__art { position: absolute; inset: 0; }
  .brand {
    position: absolute; color: var(--white);
    font-weight: 700; line-height: 1; letter-spacing: -0.5px;
  }
  .brand--top { left: 40px; top: 38px; font-size: 30px; }
  .brand--bottom { left: 62px; top: 906px; font-size: 22px; }
  .intro {
    position: absolute; left: 72px; width: 528px; top: 110px;
    color: var(--white); font-size: 14.4px; line-height: 19.4px;
    text-align: justify; text-align-last: center;
    hyphens: auto; -webkit-hyphens: auto;
  }
  .intro strong, .outro strong { font-weight: 700; }
  .advantages__title {
    position: absolute; left: 40px; top: 480px; width: 455px;
    color: var(--red); font-size: 18.5px; font-weight: 600;
    padding-bottom: 6px; border-bottom: 1.5px solid var(--red);
  }
  .advantages__col { position: absolute; list-style: none; }
  .advantages__col--left { left: 40px; top: 535px; width: 296px; }
  .advantages__col--right { left: 352px; top: 537px; width: 294px; }
  .benefit {
    position: relative; padding-left: 22px; margin-bottom: 14px;
    font-size: 11px; line-height: 13.8px; letter-spacing: -0.2px;
    hyphens: auto; -webkit-hyphens: auto;
  }
  .advantages__col--right .benefit { margin-bottom: 16px; }
  .benefit__arrow { position: absolute; left: 0; top: 50%; transform: translateY(-50%); width: 10px; height: 16px; }
  .benefit__name { color: var(--red); }
  .benefit__text { color: var(--ink); }
  .benefit__text + .benefit__text { margin-top: 14px; }
  .outro {
    position: absolute; left: 72px; width: 528px; top: 832px;
    color: var(--white); font-size: 14px; line-height: 13.6px;
    text-align: justify; text-align-last: center;
    hyphens: auto; -webkit-hyphens: auto;
  }
</style>
</head>
<body>
<main class="flyer">
  <svg class="flyer__art" width="670" height="960" viewBox="0 0 670 960">
    <defs>
      <linearGradient id="photoTone" x1="0" y1="0" x2="1" y2="1">
        <stop offset="0" stop-color="var(--photo-light)"/>
        <stop offset="0.5" stop-color="#b4b4b4"/>
        <stop offset="1" stop-color="var(--photo-dark)"/>
      </linearGradient>
    </defs>
    <rect class="flyer__photo" width="670" height="456" fill="url(#photoTone)" role="img" aria-label="Black and white photo of two wall-mounted security cameras on a building corner, with a dome camera above"/>
    <polygon class="flyer__header-band" points="0,0 670,0 670,198 335,416 0,198" fill="var(--red-overlay)"/>
    <polygon class="flyer__footer-band" points="0,819 335,760 670,819 670,960 0,960" fill="var(--red-deep)"/>
  </svg>

  <div class="brand brand--top">Rampart Group</div>

  <p class="intro"><strong>Rampart Group</strong> offers remove <strong>live video monitoring</strong>. This program has some key advantages for some customers. We use high quality components to monitor your site remotely and respond to analytic based alarms. <strong>Our in-house operators</strong> verify all alarms and communicate via loudspeaker with intruders while co-ordinating security and <strong>police response.</strong></p>

  <h2 class="advantages__title">ADVANTAGES OF LIVE VIDEO MONITORING</h2>

  <ul class="advantages__col advantages__col--left">
    <li class="benefit"><svg class="benefit__arrow" viewBox="0 0 10 16"><path d="M1 1 L8 8 L1 15" fill="none" stroke="var(--red)" stroke-width="2.5"/></svg>
      <div class="benefit__name">Save money</div><div class="benefit__text">Can be half the cost of a security</div></li>
    <li class="benefit"><svg class="benefit__arrow" viewBox="0 0 10 16"><path d="M1 1 L8 8 L1 15" fill="none" stroke="var(--red)" stroke-width="2.5"/></svg>
      <div class="benefit__name">Theft reduction</div><div class="benefit__text">Cameras and signage deter theft. Live operator speaking to intruder stops thefts.</div></li>
    <li class="benefit"><svg class="benefit__arrow" viewBox="0 0 10 16"><path d="M1 1 L8 8 L1 15" fill="none" stroke="var(--red)" stroke-width="2.5"/></svg>
      <div class="benefit__name">Flat Monthly Fee</div><div class="benefit__text">Monthly fee is all inclusive of all equipment; setup; monitoring; troubleshooting</div></li>
    <li class="benefit"><svg class="benefit__arrow" viewBox="0 0 10 16"><path d="M1 1 L8 8 L1 15" fill="none" stroke="var(--red)" stroke-width="2.5"/></svg>
      <div class="benefit__name">Several Set of Eyes</div><div class="benefit__text">Having several cameras with analytics is like having several security staff posted at various positions at all times on your property.</div></li>
  </ul>

  <ul class="advantages__col advantages__col--right">
    <li class="benefit"><svg class="benefit__arrow" viewBox="0 0 10 16"><path d="M1 1 L8 8 L1 15" fill="none" stroke="var(--red)" stroke-width="2.5"/></svg>
      <div class="benefit__name">Timely Police Response</div><div class="benefit__text">With a verified crime in progress the police will respond much quicker</div></li>
    <li class="benefit"><svg class="benefit__arrow" viewBox="0 0 10 16"><path d="M1 1 L8 8 L1 15" fill="none" stroke="var(--red)" stroke-width="2.5"/></svg>
      <div class="benefit__name">Continuous Video Recording</div><div class="benefit__text">System can be set to record 24/7 to ensure evidence of incidents are available</div></li>
    <li class="benefit"><svg class="benefit__arrow" viewBox="0 0 10 16"><path d="M1 1 L8 8 L1 15" fill="none" stroke="var(--red)" stroke-width="2.5"/></svg>
      <div class="benefit__name">Flexibility</div><div class="benefit__text">System can be set up in environments where no power is available by using solar and batteries.</div><div class="benefit__text">System can be moved and altered as projects change and evolve</div></li>
  </ul>

  <p class="outro"><strong>All aspects of our video monitoring</strong> is managed in <strong>house.</strong> Installation, video monitoring; mobile responses are all in house. We do not outsource anything which ensures we provide the <strong>highest</strong> level of service to <strong>our customers.</strong></p>

  <div class="brand brand--bottom">Rampart Group</div>
</main>
</body>
</html>
```